Broschüre für Nachlassverwaltung und Testamentsvollstreckung
Zielgruppe
Nachlassverwaltung und Testamentsvollstreckung
Aufgabenstellung
Ich brauche:
1. ) Präsentationsmappe: mit Visitenkartentasche innenliegend links unten, Endformat: 440 x 307 mm
Endformat: 440 x 307 mm
Seitenanzahl: 2-seitig
Farbigkeit: 4/4-farbig
Diese Beschreibung bezieht sich auf unsere Topseller-Sorte 0,40 mm starker Chromokarton 255g (zertifiziert mit GWNA-Siegel für Nachhaltigkeit), hohe Steifigkeit mit 1,6-fachem Volumen. Weitere Sorten finden Sie in der Produktauswahl.
Hochwertige Mappe für DIN A4, 4/4 farbig (Außen- und Innenseite bedruckt)
0,40 mm starker Chromokarton 255g (zertifiziert mit GWNA-Siegel für Nachhaltigkeit), hohe Steifigkeit mit 1,6-fachem Volumen
Datenformat: 45,0 x 31,7 cm
Endformat: 44,0 x 30,7 cm
2. ) Ringordner
Ringbuch (2-Loch) bis zu 400 DIN A4 Blätter
Außen- und Innenseite farbig bedruckt (4/4)
Hochwertiger Qualitätsdruck mit Glanzfolie veredelt
4/4 farbig außen und innen
Endformat: 61,5 cm x 31,5 cm
geschlossenes Endformat: 28,2 cm x 31,5 cm
Datenformat: 65,1 cm x 35,1 cm
Folgende Dienstleistungen sollten mit aufgeführt sein:
- Testamentsvollstreckung
- Nachlassabwicklung
- Nachlassverwaltung
- Nachlasspflege

```html
<!DOCTYPE html>
<html lang="de">
<head>
<meta charset="utf-8">
<title>Levan Erbschaftspflege – Mappe</title>
<link rel="stylesheet" href="https://fonts.googleapis.com/css2?family=Cinzel:wght@400;700&family=Libre+Baskerville:wght@700&display=swap">
<style>
  :root {
    --backdrop: #cccccc;
    --slate: #4a4b48;
    --amber: #e8922c;
    --amber-light: #f9ae3f;
    --amber-deep: #e7852a;
    --paper: #ffffff;
    --ink: #4a4b48;
  }
  * { margin: 0; padding: 0; box-sizing: border-box; }
  html, body { width: 667px; height: 1200px; overflow: hidden; }
  body { background: var(--backdrop); position: relative; font-family: "Cinzel", serif; }

  .sheet { position: absolute; left: 29px; width: 609px; background: var(--slate); overflow: hidden; }
  .sheet--outer { top: 504px; height: 316px; }
  .sheet--inner { top: 842px; height: 313px; }

  .brand {
    position: absolute; display: flex; align-items: center; gap: 6px;
    color: var(--amber); font-family: "Cinzel", serif; font-weight: 400;
    font-size: 11px; letter-spacing: 0.2px; white-space: nowrap;
  }
  .brand__mark { width: 7px; height: 7px; background: var(--amber); flex: none; }
  .brand--back { left: 32px; top: 234px; }
  .brand--front { left: 372px; top: 37px; }

  .spine-title {
    position: absolute; left: 300px; top: 34px; width: 18px; height: 214px;
    writing-mode: vertical-rl; color: var(--amber);
    font-family: "Cinzel", serif; font-size: 14.5px; letter-spacing: 0.6px; white-space: nowrap;
  }

  .band-rule { position: absolute; left: 0; right: 0; top: 272px; height: 1px; background: var(--amber); }

  .contact {
    position: absolute; top: 289px; color: var(--amber);
    font-family: "Libre Baskerville", serif; font-weight: 700; font-size: 5.2px;
  }
  .contact--mail { left: 23px; }
  .contact--web { left: 169px; }

  .inner-title {
    position: absolute; left: 24px; top: 30px; color: var(--amber);
    font-family: "Cinzel", serif; font-weight: 700; font-size: 23px; line-height: 29px;
  }

  .pocket { position: absolute; left: 0; top: 0; }
  .pocket__rule { stroke: #e8922c; stroke-width: 1; }
  .pocket__card { fill: #ffffff; }

  .card-brand {
    position: absolute; left: 42px; top: 263px; display: flex; align-items: center; gap: 2px;
    color: var(--ink); font-family: "Cinzel", serif; font-weight: 400; font-size: 4px; white-space: nowrap;
  }
  .card-brand .brand__mark { width: 3px; height: 3px; background: var(--ink); }
</style>
</head>
<body>

  <section class="sheet sheet--outer" aria-label="Außenseite der Mappe">
    <div class="brand brand--back"><span class="brand__mark"></span>LEVAN ERBSCHAFTSPFLEGE</div>

    <div class="spine-title">Fide et Diligentia</div>

    <div class="brand brand--front"><span class="brand__mark"></span>LEVAN ERBSCHAFTSPFLEGE</div>

    <div class="band-rule"></div>
    <p class="contact contact--mail">info@levan-erbe.de</p>
    <p class="contact contact--web">www.levan-erbe.de</p>
  </section>

  <section class="sheet sheet--inner" aria-label="Innenseite der Mappe">
    <h1 class="inner-title">Fide et<br>Diligentia</h1>

    <svg class="pocket" width="609" height="313" viewBox="0 0 609 313" aria-label="Visitenkartentasche">
      <defs>
        <linearGradient id="pocket-fill" x1="0" y1="0" x2="1" y2="0">
          <stop offset="0" stop-color="#f9ae3f"/>
          <stop offset="1" stop-color="#e7852a"/>
        </linearGradient>
      </defs>
      <path d="M0,241 H165 Q190,241 203,262 L236,313 H0 Z" fill="url(#pocket-fill)"/>
      <line class="pocket__rule" x1="209" y1="272.5" x2="609" y2="272.5"/>
      <path class="pocket__card" d="M37,244 H145 V289 L136,298 H32 V249 Z"/>
    </svg>

    <div class="card-brand"><span class="brand__mark"></span>LEVAN ERBSCHAFTSPFLEGE</div>
  </section>

</body>
</html>
```